immediate money for financial solutions

We need a Clean yet, eye catching, Business Card denoting a professional financial/tech firm. The front should have our logo and the notion that we are money lenders that get business loans quickly & easily. Maybe shade the colors of our logo. We are opened, but not committed to an unusual shaped card. The Back Should have our Business Contact Info & logo found on our website's front page: KORVANTINC.COM

Financial

```html
<!DOCTYPE html>
<html lang="en">
<head>
<meta charset="utf-8">
<title>Korvant Inc – Business Card</title>
<link rel="stylesheet" href="https://fonts.googleapis.com/css2?family=Gelasio:wght@400;700&display=swap">
<style>
  :root {
    --card-bg: #f5fdd0;
    --frame: #0f4320;
    --brand-green: #33dd00;
    --logo-green: #2fc43a;
  }
  * { margin: 0; padding: 0; box-sizing: border-box; }
  html, body {
    width: 1200px;
    height: 686px;
    overflow: hidden;
    background: var(--card-bg);
  }
  .card {
    position: relative;
    width: 1200px;
    height: 686px;
    background: var(--card-bg);
    border: 9px solid var(--frame);
    font-family: "Gelasio", Georgia, serif;
    color: var(--brand-green);
    text-align: center;
  }
  .card > * {
    position: absolute;
    left: 0;
    right: 0;
    line-height: 1;
  }
  .brand-mark {
    top: 100px;
    display: flex;
    justify-content: center;
  }
  .brand-mark span {
    width: 30px;
    height: 30px;
    background: var(--logo-green);
  }
  .brand-name {
    top: 143px;
    font-size: 27px;
    color: var(--logo-green);
    letter-spacing: 0.5px;
  }
  .brand-tagline {
    top: 176px;
    font-size: 16px;
    color: var(--logo-green);
  }
  .person-name {
    top: 282px;
    font-size: 68px;
    font-weight: 700;
  }
  .person-role {
    top: 356px;
    font-size: 43px;
  }
  .person-phone {
    top: 415px;
    font-size: 43px;
  }
  .contact-email {
    font-size: 27px;
    font-weight: 700;
  }
  .contact-email.personal { top: 492px; }
  .contact-email.general { top: 541px; }
</style>
</head>
<body>
  <main class="card">
    <div class="brand-mark" aria-hidden="true"><span></span></div>
    <p class="brand-name">KORVANT INC</p>
    <p class="brand-tagline">READY-SET-GO</p>
    <h1 class="person-name">Daniel Marsh</h1>
    <p class="person-role">President / Lender</p>
    <p class="person-phone">555.014.2287</p>
    <p class="contact-email personal">Daniel@korvantinc.com</p>
    <p class="contact-email general">ATMinfo@korvantinc.com</p>
  </main>
</body>
</html>
```